Design for Agenda app (online tool) (#102244)

Url of the app: http://notes.bluefernlab.dk

It currently has 3 main parts:
- Front: http://fernhost.dk/screencast/2015-12-01_12-53-36.png
- Dashboard: http://fernhost.dk/screencast/2015-12-01_12-54-16.png
- Meeting page: http://fernhost.dk/screencast/2015-12-01_12-54-53.png

The idea of the app is to have virtual meetings with other people, to take notes/minutes online and to share what is written.

Unregistered users can see only the front.

Registered users can see front, their own dashboard and the meetings which they created or to which they were invited.

The meeting itself has two roles - minute taker an attendee. The attendee can edit only the agenda so he should have different view for the other parts of the meeting compared to the minute taker who can edit everything.

In this doc it is described what are the elements per page which we want to have
https://files.example-docs.net/d/7qXk2LmPz9RtYv4NcBw8HsJd3FgA6eUo1KtQ5WnZ0yE/edit?usp=sharing

As you can see, there is some inconsistency between the front page and the rest of the app. We would like to make it look professional and consistent on all places.

Goal: Get new responsive design where all main parts(front page, dashboard page, meeting page and profile page) will be consistent with each other.

The design should be clean, simple and with very friendly UX.
Updates

Industry/Entity Type

Online

Number of Pages Required

3 page

Font styles to use
Sans Serif

Requirements
Must have
• - Clean and simple
• - Very friendly UX

```html
<!DOCTYPE html>
<html lang="en">
<head>
<meta charset="utf-8">
<title>Bluefern Agenda</title>
<link href="https://fonts.googleapis.com/css2?family=Lato:wght@300;400;700&display=swap" rel="stylesheet">
<style>
:root{
  --accent:#ff5314;
  --ink:#ffffff;
  --ink-soft:#e6e0da;
  --nav-tab:#3f3a36;
  --bar:#2e2b29;
  --rule:#8a837d;
  --bubble:rgba(40,36,34,.72);
  --photo-top:#6e625a;
  --photo-mid:#847569;
  --photo-low:#4d4440;
}
*{margin:0;padding:0;box-sizing:border-box}
html,body{width:1200px;height:800px;overflow:hidden}
body{font-family:"Lato",sans-serif;color:var(--ink);position:relative;background:var(--bar)}
.hero-photo{position:absolute;inset:0;background:linear-gradient(180deg,var(--photo-top) 0%,var(--photo-mid) 45%,var(--photo-low) 100%)}
.topbar{position:absolute;left:0;top:0;width:1200px;height:92px;border-bottom:2px solid var(--rule);background:rgba(60,54,50,.35)}
.nav{position:absolute;left:130px;top:0;display:flex;gap:2px}
.nav-item{height:91px;background:var(--nav-tab);color:var(--ink-soft);display:flex;flex-direction:column;align-items:center;justify-content:flex-end;padding-bottom:12px;font-size:15px;font-weight:300;gap:10px}
.nav-item svg{width:28px;height:28px}
.nav-item.is-active{background:var(--accent);color:var(--ink);font-weight:400}
.nav-home{width:87px}.nav-about{width:104px}.nav-features{width:102px}
.social{position:absolute;right:139px;top:18px;display:flex;gap:14px}
.social span{width:12px;height:12px;border:1.5px solid var(--ink);border-radius:50%}
.account{position:absolute;right:139px;top:50px;font-size:15px;font-weight:300;color:var(--ink-soft)}
.account a{color:var(--ink);font-weight:700;text-decoration:none;border-bottom:1px dotted var(--ink);padding-bottom:2px;margin:0 4px}
.account a:last-child{margin-right:0}
.brand-circle{position:absolute;left:524px;top:142px;width:150px;height:150px;border-radius:50%;background:var(--bubble)}
.brand-name{position:absolute;left:472px;top:271px;width:256px;height:60px;border-radius:30px;background:var(--bubble);font-size:31px;font-weight:300;display:flex;align-items:center;justify-content:center}
.headline{position:absolute;left:0;width:1200px;top:400px;text-align:center;font-size:76px;font-weight:300;text-shadow:0 2px 4px rgba(0,0,0,.35)}
.tagline{position:absolute;left:0;width:1200px;top:500px;text-align:center;font-size:24px;font-weight:400;text-shadow:0 2px 3px rgba(0,0,0,.5)}
.cta{position:absolute;left:450px;top:576px;width:300px;height:56px;border-radius:28px;background:var(--accent);font-size:17px;display:flex;align-items:center;justify-content:center;letter-spacing:.2px}
.footer{position:absolute;left:0;top:732px;width:1200px;height:68px;border-top:2px solid var(--rule);background:var(--bar);display:flex;align-items:center;justify-content:center;font-size:14px;font-weight:400}
.footer .owner{border-bottom:1px dotted var(--ink);margin-left:4px}
.footer .sep{margin:0 7px}
</style>
</head>
<body>
<div class="hero-photo" role="img" aria-label="Photo of a bright modern open-plan office with desks, monitors and chairs, toned in warm brown"></div>

<header class="topbar">
  <nav class="nav">
    <div class="nav-item nav-home is-active">
      <svg viewBox="0 0 28 28" fill="none" stroke="currentColor" stroke-width="1.6"><path d="M3 14 14 4l11 10"/><path d="M6 12v12h6v-7h4v7h6V12"/></svg>
      Home
    </div>
    <div class="nav-item nav-about">
      <svg viewBox="0 0 28 28" fill="currentColor"><circle cx="14" cy="9" r="3.5"/><path d="M8 24v-6a6 6 0 0 1 12 0v6z"/><circle cx="6" cy="11" r="2.6"/><path d="M1 23v-4a5 5 0 0 1 7-4v8z"/><circle cx="22" cy="11" r="2.6"/><path d="M27 23v-4a5 5 0 0 0-7-4v8z"/></svg>
      About Us
    </div>
    <div class="nav-item nav-features">
      <svg viewBox="0 0 28 28" fill="none" stroke="currentColor" stroke-width="1.6"><circle cx="10" cy="17" r="6" stroke-dasharray="3 1.6"/><circle cx="10" cy="17" r="2.2"/><circle cx="21" cy="7" r="4" stroke-dasharray="2 1.3"/><circle cx="21" cy="7" r="1.4"/></svg>
      Features
    </div>
  </nav>
  <div class="social"><span></span><span></span><span></span></div>
  <p class="account">Don't have account? <a href="#">Sign Up</a> Or <a href="#">Sign In</a></p>
</header>

<div class="brand-circle"></div>
<div class="brand-name">Bluefern Agenda</div>

<h1 class="headline">Meet, Note, Share!</h1>
<p class="tagline">Take Notes Online For All Kind Of Meetings. It Has Never Been That Easy. Give It A Try!</p>
<div class="cta">ENTER BLUEFERN ADENDA</div>

<footer class="footer">Copyright 2015 <span class="owner">Bluefern Agenda</span><span class="sep">|</span>All Rights Reserved.</footer>
</body>
</html>
```